A simple Chatterbook Ad (not Chatterbook Page) for weight loss surgery

It’s a simple ad in terms of the text.

The text should say:
Curious about weight loss surgery?
This 30 second quiz will tell you which procedure will suit you best

I'm open to variations in the text if it is thought to enhance the ad.

Targeted towards obese individuals who have been unable to lose weight with diet and exercise. My industry is weight loss surgery – webpage www.marcusbellweather.com.au. Clicking the ad leads to a quiz on my webpage relating to weight loss surgery. Most frequent users of this service are females (75%) between ages of 35 and 55 years.

Successful weight loss surgery can enable individuals who have been unable to lose weight to lose a substantial amount of the excess weight they are carrying to be healthier and happier.

```html
<!DOCTYPE html>
<html lang="en">
<head>
<meta charset="UTF-8">
<title>Weight Loss Surgery Quiz Ad</title>
<link rel="stylesheet" href="https://fonts.googleapis.com/css2?family=Bodoni+Moda:wght@400&family=Poppins:wght@500&display=swap">
<style>
  :root {
    --bg-top: #e6e4df;
    --bg-mid: #dde3ee;
    --bg-low: #e9ecf2;
    --gown: #cdd6e8;
    --headline-grey: #555555;
    --headline-teal: #0e8278;
    --pill-bg: #a9aaab;
    --pill-text: #f7f5f0;
    --model-tone-a: #3f7590;
    --model-tone-b: #2f6884;
  }
  * { margin: 0; padding: 0; box-sizing: border-box; }
  html, body { width: 1200px; height: 1200px; overflow: hidden; }
  .ad {
    position: relative;
    width: 1200px;
    height: 1200px;
    overflow: hidden;
    background: linear-gradient(180deg, var(--bg-top) 0%, var(--bg-mid) 45%, var(--bg-low) 100%);
  }
  .surgeons-backdrop {
    position: absolute;
    inset: 0;
    background:
      radial-gradient(ellipse 300px 260px at 480px 230px, rgba(120,130,160,0.35), transparent 70%),
      radial-gradient(ellipse 380px 300px at 1000px 280px, rgba(170,185,225,0.35), transparent 70%),
      radial-gradient(ellipse 700px 500px at 700px 900px, var(--gown), transparent 75%);
    opacity: 0.8;
  }
  .model-photo {
    position: absolute;
    left: 132px;
    top: 95px;
    width: 242px;
    height: 1035px;
    border-radius: 24px;
    background: linear-gradient(180deg, var(--model-tone-a) 0%, var(--model-tone-b) 100%);
    opacity: 0.55;
  }
  .headline {
    font-family: 'Bodoni Moda', serif;
    font-weight: 400;
  }
  .headline-line {
    position: absolute;
    left: 420px;
    width: 750px;
    text-align: center;
    white-space: nowrap;
    line-height: 1;
  }
  .headline-lead {
    top: 328px;
    color: var(--headline-grey);
    font-size: 110px;
    letter-spacing: -1px;
  }
  .headline-focus {
    color: var(--headline-teal);
    font-size: 95px;
    letter-spacing: -1px;
  }
  .headline-focus.line-one { top: 452px; }
  .headline-focus.line-two { top: 558px; left: 415px; }
  .quiz-pill {
    position: absolute;
    left: 491px;
    top: 761px;
    width: 614px;
    height: 125px;
    border-radius: 32px;
    background: var(--pill-bg);
    display: flex;
    align-items: center;
    justify-content: center;
    text-align: center;
    font-family: 'Poppins', sans-serif;
    font-weight: 500;
    font-size: 31px;
    line-height: 1.3;
    color: var(--pill-text);
  }
</style>
</head>
<body>
  <main class="ad">
    <div class="surgeons-backdrop" role="img" aria-label="Soft-focus photo of surgeons in scrubs and caps in an operating theatre"></div>
    <div class="model-photo" role="img" aria-label="Photo of a smiling woman in teal activewear standing barefoot on a pink bathroom scale"></div>
    <h1 class="headline">
      <span class="headline-line headline-lead">Curious about</span>
      <span class="headline-line headline-focus line-one">WEIGHT LOSS</span>
      <span class="headline-line headline-focus line-two">SURGERY?</span>
    </h1>
    <p class="quiz-pill">This 30 second quiz will tell you<br>which procedure will suit you best</p>
  </main>
</body>
</html>
```